Automotive Restoration Magazine Design Project

I am in need of a full page ad being designed for my company. We are T & K Autoworks, specializing in Muscle Car Restoration, Classic Automobile Restoration, & Turnkey Racecars. T & K Autoworks Inc. has 17 highly skilled technicians and fabricators working in our shop to give your muscle car or classic what it truly deserves. We specialize in Corvana, Dravette, and Bisonte restoration.

This will be a full page ad in Bellweather Vintage Motor Journal. The details for the ad specs are listed in the media kit attachment. Sorry for the rush as this was a last minute decision to run this ad.

What we like to crisp, clean feel similar to how our web site is. Nothing too gaudy or flashy but elegant and professional. I have attached some info that you are welcome to use in the ad also feel free to use any information listed on the website. Thanks and please don't hesitate with any questions.
Updates

Please feel free to pull the cars from the photos uploaded as desired. Thanks!

Target Market(s)

Mainly Male ages 35-65

Industry/Entity Type

Automotive

Requirements
Must have
• Web site- www.tandkautoworks.example
Logo
Facility Size Listed 60,000 sq ft
17 Employees
Location
Chatterbook and chirpit logos
Phone number and contact info from our web site
Our Services: Auto Restoration, Muscle Cars, Street Rods, & Classics.
Nice to have
• company colors are usually black and red but I am not stuck on that

```html
<!DOCTYPE html>
<html lang="en">
<head>
<meta charset="utf-8">
<title>T &amp; K Autoworks – Full Page Ad</title>
<link rel="stylesheet" href="https://fonts.googleapis.com/css2?family=Abril+Fatface&family=Archivo+Black&family=Questrial&family=Montserrat:wght@700&display=swap">
<style>
  :root {
    --ink: #111111;
    --red: #d6002a;
    --paper: #ffffff;
    --stage: #f2f2f2;
    --footer: #1b1b1b;
    --car-dark: #3a3b3d;
    --car-light: #8c8d90;
    --skin: #d9a98c;
    --suit: #2b2b2b;
  }
  * { margin: 0; padding: 0; box-sizing: border-box; }
  html, body { width: 1200px; height: 1000px; overflow: hidden; background: var(--stage); }
  .ad-page {
    position: absolute; left: 250px; top: 0; width: 705px; height: 1000px;
    background: var(--paper); overflow: hidden;
  }
  .ad-page > * { position: absolute; white-space: nowrap; line-height: 1; }
  .thin { font-family: "Questrial", sans-serif; font-weight: 400; }
  .fat-serif { font-family: "Abril Fatface", serif; }
  .heavy { font-family: "Archivo Black", sans-serif; }
  .red { color: var(--red); }
  .black { color: var(--ink); }

  .headline-initial { left: 22px; top: 38px; font-size: 172px; letter-spacing: -4px; }
  .headline-auto { left: 170px; top: 66px; font-size: 56px; }
  .headline-restoration { left: 155px; top: 113px; font-size: 68px; letter-spacing: -1px; }

  .service-classics { left: 36px; top: 170px; font-size: 66px; letter-spacing: -1.5px; }
  .service-street { left: 15px; top: 220px; font-size: 60px; }
  .service-rods { left: 210px; top: 224px; font-size: 56px; }
  .service-muscle { left: 470px; top: 166px; font-size: 54px; letter-spacing: -0.5px; }
  .cars-initial { left: 352px; top: 160px; font-size: 140px; }
  .cars-rest { left: 470px; top: 176px; font-size: 122px; letter-spacing: -1px; }

  .stat-area { left: 12px; top: 282px; font-size: 82px; }
  .stat-staff-count { left: 318px; top: 284px; font-size: 28px; }
  .stat-staff-label { left: 370px; top: 274px; font-size: 48px; }
  .stat-area-unit { left: 318px; top: 310px; font-size: 42px; letter-spacing: 1px; }

  .car-photo { left: 85px; top: 385px; width: 550px; height: 225px; }
  .keys-photo { left: 0; top: 665px; width: 250px; height: 185px; }

  .social { top: 715px; display: flex; flex-direction: column; align-items: center; gap: 10px; }
  .social-chatterbook { left: 265px; width: 90px; }
  .social-chirpit { left: 370px; width: 90px; }
  .social-dot { width: 80px; height: 80px; border-radius: 50%; background: #e4e4e4; box-shadow: inset 0 0 0 6px #ffffff; }
  .social-chatterbook .social-dot { background: #3b5998; }
  .social-chirpit .social-dot { background: #1da1f2; }
  .social-name { font-family: "Abril Fatface", serif; font-size: 16px; color: var(--ink); }

  .brand-mark { left: 475px; top: 650px; width: 215px; height: 215px; }
  .brand-name {
    left: 507px; top: 730px; width: 151px; text-align: center;
    font-size: 24px; line-height: 1.15; white-space: normal;
  }

  .contact-row { left: 8px; top: 880px; width: 695px; display: flex; justify-content: space-between; align-items: center; }
  .contact-item { display: flex; align-items: center; gap: 6px; font-family: "Abril Fatface", serif; font-size: 28px; color: var(--ink); }
  .contact-dot { width: 26px; height: 26px; border-radius: 50%; background: #2d4fa3; }

  .footer-band { left: 0; top: 922px; width: 705px; height: 78px; background: var(--footer); text-align: center; }
  .footer-web { display: block; margin-top: 12px; font-family: "Montserrat", sans-serif; font-weight: 700; font-size: 28px; color: var(--paper); letter-spacing: 0.5px; }
  .footer-web .red { color: var(--red); }
  .footer-address { display: block; margin-top: 8px; font-family: "Abril Fatface", serif; font-size: 20px; color: var(--paper); }
</style>
</head>
<body>
<main class="ad-page">
  <div class="headline-initial thin red">R</div>
  <div class="headline-auto fat-serif black">Auto</div>
  <div class="headline-restoration thin red">estoration</div>

  <div class="service-classics heavy black">Classics</div>
  <div class="service-street fat-serif red">Street</div>
  <div class="service-rods fat-serif black">Rods</div>
  <div class="cars-initial thin black">C</div>
  <div class="cars-rest thin black">ars</div>
  <div class="service-muscle heavy red">Muscle</div>

  <div class="stat-area fat-serif black">60.000</div>
  <div class="stat-staff-count fat-serif red">17</div>
  <div class="stat-staff-label fat-serif black">Employees</div>
  <div class="stat-area-unit fat-serif red">SQ FT</div>

  <svg class="car-photo" viewBox="0 0 550 225" role="img" aria-label="Restored black muscle car with red stripes, three-quarter front view">
    <defs>
      <linearGradient id="carTone" x1="0" y1="0" x2="1" y2="1">
        <stop offset="0" stop-color="var(--car-dark)"/>
        <stop offset="1" stop-color="var(--car-light)"/>
      </linearGradient>
    </defs>
    <rect width="550" height="225" rx="30" fill="url(#carTone)"/>
  </svg>

  <svg class="keys-photo" viewBox="0 0 250 185" role="img" aria-label="Hand in a suit sleeve holding out car keys">
    <defs>
      <linearGradient id="keysTone" x1="0" y1="0" x2="1" y2="0">
        <stop offset="0" stop-color="var(--suit)"/>
        <stop offset="1" stop-color="var(--skin)"/>
      </linearGradient>
    </defs>
    <rect width="250" height="185" fill="url(#keysTone)"/>
  </svg>

  <div class="social social-chatterbook"><span class="social-dot"></span><span class="social-name">Chatterbook</span></div>
  <div class="social social-chirpit"><span class="social-dot"></span><span class="social-name">chirpit</span></div>

  <svg class="brand-mark" viewBox="0 0 215 215" aria-hidden="true">
    <circle cx="107.5" cy="107.5" r="100" fill="none" stroke="var(--ink)" stroke-width="6"/>
  </svg>
  <div class="brand-name heavy red">T &amp; K Autoworks</div>

  <div class="contact-row">
    <span class="contact-item"><span class="contact-dot"></span>555.201.0143</span>
    <span class="contact-item"><span class="contact-dot"></span>555.201.0144</span>
    <span class="contact-item">
      <svg width="16" height="28" viewBox="0 0 16 28" aria-hidden="true">
        <rect x="1" y="1" width="14" height="26" rx="3" fill="var(--ink)"/>
        <rect x="3" y="4" width="10" height="9" fill="#ffffff"/>
        <rect x="3" y="16" width="10" height="8" fill="#777777"/>
      </svg>555.201.0145</span>
  </div>

  <footer class="footer-band">
    <span class="footer-web">WWW.<span class="red">TANDKAUTOWORKS</span>.EXAMPLE</span>
    <span class="footer-address">4120 Quarry Hill Road Dorset, Maryland 21600</span>
  </footer>
</main>
</body>
</html>
```